Book Cover Design - Uncovering Weight Loss Secrets

I need a book cover design for a book called 'Folding The Map'. It is a book that goes through all of the secrets to weight loss, without any crazy shakes or workouts or pills or potions. The book is really focused on helping people understand that Weight loss is simple and has more to do with our mindset as well as the food we were eating. It is about taking personal responsibility not looking for the next fancy revolutionary product that is going to help them magically melt the fat away. The book is pragmatic in nature and breaks down in simple terms how we can lose weight and keep it off for the rest of our lives. It shows the user that it is simple to lose weight, but it takes effort. They should stop looking for a quick fix when it comes to weight loss but instead eat healthy for the rest of their lives.
The book is intended to be hard-hitting no holds barred approach. The book has the same title as my business name. I will attach the current logo that we use in the business. This doesn't need to be on the front of the book maybe at the back down the bottom somewhere.
I am looking to have both an e-book cover and a standard printed book cover.
I don't have any colours in mind, my logo can be adapted to be different colours or just white.
The message that I am wanting people to feel when they see my book, is that all these Weightloss fads are a joke, that I know the secrets that will get them to their weight loss goal even if they fail at everything else before.
On the cover it should say the following.
FOLDING THE MAP
Uncovering the Weight Loss Secrets
The big companies have been trying to keep hidden for years!
COLIN MAYHEW
People who have failed many times trying to lose weight & need help
Weight Loss

```html
<!DOCTYPE html>
<html lang="en">
<head>
<meta charset="UTF-8">
<title>Folding The Map — Book Cover</title>
<link href="https://fonts.googleapis.com/css2?family=Oswald:wght@500;600;700&display=swap" rel="stylesheet">
<style>
  :root {
    --stage: #3a3a3a;
    --paper: #e6e6ea;
    --teal: #0e4255;
    --teal-band: #0b3b4c;
    --amber: #e09a0c;
    --skin-light: #c9a893;
    --skin-mid: #a98a76;
    --skin-dark: #7d6657;
    --iron: #4a4744;
    --brass: #6e6440;
  }
  * { margin: 0; padding: 0; box-sizing: border-box; }
  html, body {
    width: 1200px;
    height: 675px;
    overflow: hidden;
    background: var(--stage);
    font-family: "Oswald", "Arial Narrow", sans-serif;
  }
  .canvas {
    position: relative;
    width: 1200px;
    height: 675px;
  }
  .cover {
    position: absolute;
    left: 390px;
    top: 37px;
    width: 420px;
    height: 600px;
    background: var(--paper);
    overflow: hidden;
  }
  .cover__photo {
    position: absolute;
    left: 0;
    top: 0;
    width: 350px;
    height: 100%;
    clip-path: polygon(0 0, 78% 0, 76% 30%, 60% 45%, 80% 60%, 100% 64%, 96% 100%, 0 100%);
    background:
      radial-gradient(ellipse 60px 80px at 83% 73%, rgba(110,100,64,0.85), rgba(110,100,64,0) 100%),
      linear-gradient(172deg,
        rgba(74,71,68,0) 0%, rgba(74,71,68,0) 36%,
        rgba(74,71,68,0.35) 40%, rgba(74,71,68,0) 46%,
        rgba(74,71,68,0) 59%, rgba(74,71,68,0.4) 63%, rgba(74,71,68,0) 68%,
        rgba(74,71,68,0) 100%),
      linear-gradient(160deg, var(--skin-mid) 0%, var(--skin-light) 35%, var(--skin-mid) 65%, var(--skin-dark) 100%);
  }
  .cover__band {
    position: absolute;
    right: 0;
    top: 0;
    width: 30px;
    height: 100%;
    background: var(--teal-band);
  }
  .title {
    position: absolute;
    left: 12px;
    right: 38px;
    top: 10px;
    text-transform: uppercase;
    font-weight: 600;
    line-height: 0.9;
  }
  .title__lead {
    display: block;
    font-size: 66px;
    white-space: nowrap;
    color: var(--amber);
  }
  .title__lead .title__the { color: var(--teal); }
  .title__main {
    display: block;
    text-align: right;
    font-size: 150px;
    font-weight: 700;
    color: var(--teal);
    line-height: 0.85;
    margin-top: -6px;
  }
  .tagline {
    position: absolute;
    right: 42px;
    top: 228px;
    width: 190px;
    text-align: right;
    text-transform: uppercase;
    color: var(--teal);
    font-weight: 500;
    line-height: 1.08;
  }
  .tagline span { display: block; }
  .tagline .t-sm { font-size: 15px; white-space: nowrap; }
  .tagline .t-md { font-size: 18px; white-space: nowrap; }
  .tagline .t-accent { color: var(--amber); font-size: 25px; font-weight: 600; }
  .tagline .t-inline { display: inline; color: var(--amber); }
  .tagline .t-big { color: var(--amber); font-size: 46px; font-weight: 600; line-height: 1; }
  .author {
    position: absolute;
    left: 0;
    right: 30px;
    bottom: 16px;
    text-align: center;
    font-size: 56px;
    font-weight: 600;
    letter-spacing: 1px;
    text-transform: uppercase;
    color: var(--teal);
    white-space: nowrap;
  }
  .author__last { color: var(--amber); }
</style>
</head>
<body>
<main class="canvas">
  <section class="cover" aria-label="Book cover: Folding The Map by Colin Mayhew">
    <div class="cover__photo" role="img" aria-label="Close-up photo of a bare torso bound by heavy iron chains, fastened at the waist with an ornate brass padlock"></div>
    <div class="cover__band"></div>

    <h1 class="title">
      <span class="title__lead">Folding <span class="title__the">The</span></span>
      <span class="title__main">Map</span>
    </h1>

    <p class="tagline">
      <span class="t-sm">Uncovering the <span class="t-inline">Weight</span></span>
      <span class="t-accent">Loss Secrets</span>
      <span class="t-md">The big companies</span>
      <span class="t-md">have been trying to</span>
      <span class="t-md">keep hidden for</span>
      <span class="t-big">Years!</span>
    </p>

    <p class="author">Colin <span class="author__last">Mayhew</span></p>
  </section>
</main>
</body>
</html>
```